Travinex - You are the Boss!

Travinex is a new Silicon Valley company, of the pelim founders from Berlin, which provides a "Shared Pioneer Circle". This platform allows the crowd to support startups with money, experts and fame. Our Vision is, that everyone should become an entrepreneur.

Pls find all brief details in the attached document
Updates

Would be nice to have a list of more social services I'm available on, like a list of pictograms of all my services:

Find me on: vooka, bramlet+, qrt, fenwix, moodrail, zupp, hvoxa, etc...

pls make sure to use the right font:
http://www.typemarlow.com/fonts/Velquin

Target Market(s)

Main target market is those already involved in the startup industry, by fundraising, investing, advising, cofounding and working. Travinex brings a totaly new transparency and collaborative way of starting companies to that business.

· Entrepreneurs (looking for funding, team and community)
· Investors (looking for hot investments and )
· Experts (workers looking for startups they can work for equity)
· Incubators & Business Schools (looking for tools to advise startups)

Industry/Entity Type

It Company

Requirements
Must have
• Pls find all brief details in the attached document
Nice to have

```html
<!DOCTYPE html>
<html lang="en">
<head>
<meta charset="utf-8">
<title>Travinex – Business Card</title>
<link rel="stylesheet" href="https://fonts.googleapis.com/css2?family=Exo+2:wght@400;600;700&display=swap">
<style>
  :root {
    --ink-dark: #3f3f41;
    --accent: #f0642d;
    --paper: #ffffff;
    --text: #444446;
    --muted: #6b6b6d;
    --backdrop: #ece8e3;
    --social-chip: #5b7fb3;
  }
  * { margin: 0; padding: 0; box-sizing: border-box; }
  html, body { width: 1200px; height: 900px; overflow: hidden; }
  body {
    background: var(--backdrop);
    font-family: "Exo 2", Arial, sans-serif;
    color: var(--text);
    position: relative;
  }
  .card {
    position: absolute;
    background: var(--paper);
    box-shadow: 0 4px 14px rgba(0,0,0,.18);
    overflow: hidden;
  }

  /* Front */
  .card-front { left: 66px; top: 70px; width: 638px; height: 364px; }
  .identity {
    position: absolute; left: 0; top: 0; width: 338px; height: 118px;
    background: var(--ink-dark); color: #fff; padding: 46px 0 0 38px;
  }
  .identity-name { font-size: 25px; font-weight: 600; letter-spacing: .5px; line-height: 30px; }
  .identity-role { font-size: 19px; font-weight: 400; line-height: 24px; }
  .identity-strip { position: absolute; left: 0; top: 118px; width: 338px; height: 9px; background: var(--accent); }
  .rule-front { position: absolute; left: 338px; top: 124px; right: 0; height: 3px; background: var(--accent); }

  .brand-mark {
    position: absolute; left: 432px; top: 88px; width: 76px; height: 76px;
    border-radius: 50%; background: var(--accent);
  }
  .brand-name {
    position: absolute; left: 358px; top: 172px;
    font-size: 40px; font-weight: 700; color: #6a6a6c; line-height: 44px;
  }
  .brand-tagline {
    position: absolute; right: 30px; top: 218px;
    font-size: 17px; color: var(--muted); line-height: 22px;
  }

  .contact { position: absolute; left: 28px; top: 204px; font-size: 15px; line-height: 22px; color: var(--text); }
  .social { list-style: none; position: absolute; left: 28px; top: 262px; font-size: 15px; }
  .social li { display: flex; align-items: center; height: 26px; }
  .social-chip { width: 18px; height: 18px; background: var(--social-chip); margin-right: 8px; border-radius: 3px; }

  /* Back */
  .card-back { left: 490px; top: 456px; width: 640px; height: 376px; }
  .back-header {
    position: absolute; left: 0; top: 0; width: 100%; height: 50px;
    background: var(--ink-dark); color: #fff; font-size: 19px; font-weight: 600;
    padding: 13px 0 0 22px;
  }
  .rule-back { position: absolute; left: 0; top: 50px; width: 100%; height: 5px; background: var(--accent); }
  .interests { list-style: none; position: absolute; left: 20px; top: 70px; font-size: 15px; line-height: 22px; }
  .interests li::before {
    content: ""; display: inline-block; width: 7px; height: 7px; border-radius: 50%;
    background: var(--accent); margin-right: 7px; vertical-align: 2px;
  }
  .join { position: absolute; left: 346px; top: 76px; color: var(--accent); font-size: 17px; font-weight: 600; line-height: 22px; }
  .faint-circle { position: absolute; left: 420px; top: 130px; width: 150px; height: 150px; border-radius: 50%; background: var(--accent); opacity: .06; }

  .notes { position: absolute; left: 22px; top: 150px; width: 296px; height: 202px; border: 2px solid var(--ink-dark); }
  .notes-title { height: 30px; background: var(--ink-dark); color: #fff; text-align: center; font-size: 17px; line-height: 30px; }
  .notes-body { padding: 10px 12px; font-size: 17px; line-height: 26px; color: #222; }

  .office { position: absolute; left: 336px; top: 218px; font-size: 15px; line-height: 22px; color: #333; }
  .office-name, .office-tagline { font-weight: 700; font-size: 16px; }
</style>
</head>
<body>

<section class="card card-front" aria-label="Business card front">
  <div class="identity">
    <p class="identity-name">Jonas Reller</p>
    <p class="identity-role">Founder and CEO</p>
  </div>
  <div class="identity-strip"></div>
  <div class="rule-front"></div>

  <span class="brand-mark"></span>
  <p class="brand-name">Travinex</p>
  <p class="brand-tagline">Build what you believe!</p>

  <div class="contact">
    <p>Mobile: xxx xxx xxxx</p>
    <p>Email: The@travinex.com</p>
  </div>
  <ul class="social">
    <li><span class="social-chip"></span>Lumio.com/jonasreller</li>
    <li><span class="social-chip"></span>linkwell.com/in/jonasreller</li>
    <li><span class="social-chip"></span>Chirpa.com/jonasreller</li>
  </ul>
</section>

<section class="card card-back" aria-label="Business card back">
  <div class="back-header">Are you interested in?</div>
  <div class="rule-back"></div>
  <div class="faint-circle"></div>

  <ul class="interests">
    <li>Starting your own Business?</li>
    <li>Investing in hot Startups?</li>
    <li>Working for the next "Lumio"?</li>
  </ul>

  <p class="join">Join us on -<br>Lumio.com/Travinex</p>

  <div class="notes">
    <div class="notes-title">Notes</div>
    <div class="notes-body">date and event of meeting,<br>keywords,<br>follow-up,</div>
  </div>

  <div class="office">
    <p class="office-name">Travinex</p>
    <p class="office-tagline">Build what you believe!</p>
    <p>Berlin - Lindenallee 24 |</p>
    <p>10117 Berlin | Germany</p>
    <p>Silicon Valley - 218 N Larkmoor Rd</p>
    <p>| Sunnyvale | CA 94086</p>
  </div>
</section>

</body>
</html>
```